Real Estate Agent needs business card design

We have logo designed already, want to have business card designed. Very interested in those smaller size business card as they look very trendy. Business name is called TOVANE REALTY

Industry/Entity Type

Business

```html
<!DOCTYPE html>
<html lang="en">
<head>
<meta charset="utf-8">
<title>Tovane Realty – Business Card</title>
<link rel="stylesheet" href="https://fonts.googleapis.com/css2?family=Cinzel:wght@400;600&family=EB+Garamond:wght@400;500&display=swap">
<style>
  :root {
    --backdrop: #2a2a2a;
    --gold: #b8894a;
    --gold-light: #d2a96b;
    --gold-dark: #8f6a38;
    --ink: #1e1e1e;
    --paper: #f4f4f2;
    --paper-shade: #e6e6e4;
    --white: #ffffff;
  }
  * { box-sizing: border-box; margin: 0; padding: 0; }
  html, body { width: 1200px; height: 997px; overflow: hidden; }
  body {
    background: var(--backdrop);
    display: flex;
    flex-direction: column;
    align-items: center;
    justify-content: center;
    gap: 40px;
    font-family: "EB Garamond", Georgia, serif;
  }
  .card {
    position: relative;
    width: 760px;
    height: 434px;
    overflow: hidden;
    box-shadow: 0 10px 30px rgba(0,0,0,.45);
  }

  /* Front */
  .card-front { color: var(--white); }
  .facet-pattern {
    position: absolute; inset: 0;
    background:
      radial-gradient(ellipse at 45% 40%, rgba(255,255,255,.18), transparent 60%),
      linear-gradient(135deg, var(--gold-light) 0%, var(--gold) 50%, var(--gold-dark) 100%);
  }
  .front-content {
    position: absolute; inset: 0;
    display: flex; flex-direction: column;
    align-items: center; justify-content: center;
    gap: 54px;
  }
  .brand-name {
    font-family: "Cinzel", "Times New Roman", serif;
    font-weight: 600;
    letter-spacing: 2px;
    display: flex; align-items: center; gap: 16px;
  }
  .front-content .brand-name { font-size: 46px; color: var(--white); margin-top: 40px; }
  .brand-mark { display: block; width: 22px; height: 22px; border-radius: 50%; background: currentColor; }
  .website { font-size: 19px; letter-spacing: 5px; }

  /* Back */
  .card-back { background: linear-gradient(160deg, var(--white) 0%, var(--paper) 55%, var(--paper-shade) 100%); color: var(--ink); }
  .card-back .brand-name {
    position: absolute; top: 78px; left: 0; right: 0;
    justify-content: center;
    font-size: 36px; color: var(--ink);
  }
  .agent {
    position: absolute; left: 150px; top: 248px;
    text-align: right; width: 220px;
  }
  .agent-name { font-size: 27px; color: var(--gold); font-weight: 500; }
  .agent-title { font-size: 17px; color: var(--ink); }
  .divider {
    position: absolute; left: 398px; top: 200px;
    width: 1.5px; height: 140px;
    background: linear-gradient(to bottom, transparent, var(--gold), transparent);
  }
  .contact { position: absolute; left: 420px; top: 196px; list-style: none; font-size: 17px; }
  .contact li { display: flex; align-items: center; gap: 12px; margin-bottom: 8px; }
  .contact-icon { width: 24px; height: 24px; flex: none; }
  .address { color: var(--gold); font-size: 18px; line-height: 1.3; margin-top: 10px; padding-left: 36px; }
  .bottom-bands { position: absolute; left: 0; bottom: 0; }
  .band-gold { fill: var(--gold); }
  .band-dark { fill: var(--ink); }
</style>
</head>
<body>
  <section class="card card-front">
    <div class="facet-pattern" role="img" aria-label="Gold faceted low-poly background pattern"></div>
    <div class="front-content">
      <h1 class="brand-name"><span class="brand-mark"></span>TOVANE REALTY</h1>
      <p class="website">www.tovanerealty.com.au</p>
    </div>
  </section>

  <section class="card card-back">
    <h2 class="brand-name">TOVANE REALTY</h2>
    <div class="agent">
      <p class="agent-name">Clara Wen</p>
      <p class="agent-title">Senior Property Consultant</p>
    </div>
    <div class="divider"></div>
    <ul class="contact">
      <li>
        <svg class="contact-icon" viewBox="0 0 24 24" aria-hidden="true">
          <circle cx="12" cy="12" r="12" fill="var(--gold)"/>
          <path d="M7 9.5c0-1.3 2-2.5 5-2.5s5 1.2 5 2.5v1h-2.5V9.6c-1.5-.5-3.5-.5-5 0v.9H7z" fill="#fff"/>
          <rect x="8" y="12" width="8" height="5" rx="1" fill="#fff"/>
        </svg>
        0412 555 730
      </li>
      <li>
        <svg class="contact-icon" viewBox="0 0 24 24" aria-hidden="true">
          <circle cx="12" cy="12" r="12" fill="var(--gold)"/>
          <rect x="6.5" y="8" width="11" height="8" fill="#fff"/>
          <path d="M6.5 8l5.5 4.5L17.5 8" fill="none" stroke="var(--gold)" stroke-width="1.2"/>
        </svg>
        clara@tovanerealty.com.au
      </li>
      <li class="address">7C, 48 Harbour Road,<br>Northbridge, NSW 2063</li>
    </ul>
    <svg class="bottom-bands" width="760" height="100" viewBox="0 0 760 100" aria-hidden="true">
      <path class="band-gold" d="M520 44 C545 44 548 18 575 18 L760 18 L760 44 Z"/>
      <path class="band-dark" d="M0 66 L500 66 C530 66 535 44 565 44 L760 44 L760 100 L0 100 Z"/>
    </svg>
  </section>
</body>
</html>
```